Consulting company needs Business Cards - rough concept provided

I'm looking for someone to take our business card idea and make is slick and polished - to communicate our high-end, sophisticated, serious consulting business. We have a rough layout we did in-house. We are open to ideas on repo-ing elements, adjusting sizes, typefaces etc... within the general concept we've already come up with. We want it to be super-clean and sophisticated. We want to keep the white backgrounds, and blue brand colors. Our goal is to print with painted blue edges on thick cardstock. Thank you!!

```html
<!DOCTYPE html>
<html lang="en">
<head>
<meta charset="utf-8">
<title>NorthQuill Business Cards</title>
<link href="https://fonts.googleapis.com/css2?family=Montserrat:wght@300;400;500;700;800&display=swap" rel="stylesheet">
<style>
  :root {
    --brand-blue: #0a9be0;
    --ink: #1d1d1d;
    --ink-soft: #3a3a3a;
    --paper: #ffffff;
    --backdrop: #2e2e2e;
  }
  * { margin: 0; padding: 0; box-sizing: border-box; }
  html, body {
    width: 1200px; height: 875px; overflow: hidden;
    background: var(--backdrop);
    font-family: "Montserrat", sans-serif;
  }
  .canvas {
    width: 1200px; height: 875px;
    display: flex; align-items: center; justify-content: center; gap: 40px;
  }
  .card {
    width: 540px; height: 309px;
    background: var(--paper);
    border: 10px solid var(--brand-blue);
    position: relative;
  }

  /* Statement side */
  .statement {
    display: flex; flex-direction: column; justify-content: center;
    padding: 0 30px; gap: 12px;
  }
  .statement-line {
    font-size: 25px; font-weight: 300; color: var(--ink-soft);
    white-space: nowrap; letter-spacing: 0.5px;
  }
  .statement-line .keyword { font-weight: 700; color: var(--brand-blue); }
  .indent-1 { padding-left: 14px; }
  .indent-2 { padding-left: 92px; }
  .indent-3 { padding-left: 110px; }

  /* Contact side */
  .contact { padding: 26px 30px 22px; }
  .wordmark {
    position: absolute; top: 28px; right: 28px;
    font-size: 52px; font-weight: 800; color: var(--brand-blue);
    letter-spacing: 1px; line-height: 1;
  }
  .name-rule {
    position: absolute; left: 30px; right: 24px; top: 140px;
    display: flex; align-items: flex-end; gap: 8px;
  }
  .name-rule .rule { flex: 1; height: 1px; background: var(--brand-blue); margin-bottom: 6px; }
  .person { text-align: left; }
  .person-name {
    font-size: 26px; font-weight: 700; color: var(--brand-blue); line-height: 1;
  }
  .person-title {
    font-size: 11px; font-weight: 500; color: var(--ink); margin-top: 3px; padding-left: 40px;
  }
  .details {
    position: absolute; left: 30px; right: 26px; bottom: 22px;
    display: flex; justify-content: space-between; align-items: flex-end;
  }
  .contact-list { list-style: none; border-top: 1px solid var(--brand-blue); padding-top: 10px; width: 240px; }
  .contact-list li {
    display: flex; align-items: center; gap: 8px;
    font-size: 12px; color: var(--ink); line-height: 1.65;
  }
  .contact-list svg { width: 11px; height: 11px; fill: var(--brand-blue); flex: none; }
  .address {
    font-style: normal; text-align: right;
    font-size: 12px; color: var(--ink); line-height: 1.5;
  }
</style>
</head>
<body>
<main class="canvas">
  <section class="card statement" aria-label="Brand statement">
    <p class="statement-line indent-1"><span class="keyword">We help</span> [target demographic]</p>
    <p class="statement-line"><span class="keyword">achieve</span> [desired emotional outcome]</p>
    <p class="statement-line indent-2"><span class="keyword">by</span> [our unique approach]</p>
    <p class="statement-line indent-3"><span class="keyword">because</span> [our brand beliefs]</p>
  </section>

  <section class="card contact" aria-label="Contact details">
    <div class="wordmark">NORTHQUILL</div>
    <div class="name-rule">
      <span class="rule"></span>
      <div class="person">
        <p class="person-name">Dana Whitlock</p>
        <p class="person-title">Brand Consultant</p>
      </div>
      <span class="rule"></span>
    </div>
    <div class="details">
      <ul class="contact-list">
        <li>
          <svg viewBox="0 0 24 24" aria-hidden="true"><path d="M6.6 10.8a15.1 15.1 0 0 0 6.6 6.6l2.2-2.2c.3-.3.7-.4 1-.2 1.1.4 2.3.6 3.6.6.6 0 1 .4 1 1V20c0 .6-.4 1-1 1A17 17 0 0 1 3 4c0-.6.4-1 1-1h3.5c.6 0 1 .4 1 1 0 1.3.2 2.5.6 3.6.1.3 0 .7-.2 1z"/></svg>
          (555) 013 4827
        </li>
        <li>
          <svg viewBox="0 0 24 24" aria-hidden="true"><path d="M2 5h20v14H2zm2 2v.5l8 5 8-5V7z"/></svg>
          dana@northquill.com
        </li>
        <li>
          <svg viewBox="0 0 24 24" aria-hidden="true"><circle cx="12" cy="12" r="10"/></svg>
          www.northquill.com
        </li>
      </ul>
      <address class="address">
        4820 Linden Ave,<br>Ste 210<br>Fairview, CA 90410
      </address>
    </div>
  </section>
</main>
</body>
</html>
```